Business Card- Can you make it cool vs boring!

Need a refresh on my business card! Want it to be modern but simple, classic and a pop of coolness! we do senior living and it is boring. but that doesn't mean our business card have to look boring! Open to two sided cards. our website is www.Bruvel-HQ.com

Target Market(s)

capital market

Industry/Entity Type

senior housing/ real estate

Contact Information for Business Card

logo/ name/ cell/ address/ www.Bruvel-HQ.com/ space for a QR code

Requirements
Must have
• maybe a QR code (do not make prominent I may not use the QR so design where it can be taken out) that link to more about us/ landing page. needs to be modern but clean
Should not have
• clip art or script

```html
<!DOCTYPE html>
<html lang="en">
<head>
<meta charset="utf-8">
<title>Bruvel Living – Business Card</title>
<link href="https://fonts.googleapis.com/css2?family=Montserrat:wght@400;500&display=swap" rel="stylesheet">
<style>
  :root{
    --stage:#434343;
    --rust:#c0501f;
    --orange-light:#df8a3a;
    --orange-mid:#d2702a;
    --orange-deep:#bf5420;
    --paper:#ffffff;
    --ink:#2b2b2b;
    --grey:#858585;
    --qr-line:#d9d9d9;
  }
  *{margin:0;padding:0;box-sizing:border-box}
  html,body{width:1200px;height:1200px;overflow:hidden}
  body{background:var(--stage);position:relative;font-family:'Montserrat',sans-serif}

  .card{position:absolute;left:206px;width:784px;height:451px;border-radius:19px;overflow:hidden}
  .card--front{top:129px}
  .card--back{top:620px;background:var(--paper)}

  .front-photo{position:absolute;inset:0;
    background:linear-gradient(100deg,var(--orange-light) 0%,var(--orange-mid) 45%,var(--orange-deep) 100%)}

  .wordmark{position:absolute;font-weight:400;line-height:1}
  .wordmark__name{display:block}
  .wordmark__sub{display:block}

  .card--front .wordmark{left:0;right:0;top:150px;color:var(--paper);text-align:center}
  .card--front .wordmark__name{font-size:108px;letter-spacing:12px;padding-left:12px}
  .card--front .wordmark__sub{font-size:30px;letter-spacing:26px;margin-top:28px;padding-left:26px}

  .card--back .wordmark{right:22px;top:38px;text-align:right}
  .card--back .wordmark__name{font-size:66px;letter-spacing:6px;color:var(--rust)}
  .card--back .wordmark__sub{font-size:18px;letter-spacing:14px;margin-top:18px;margin-right:-2px;color:var(--grey)}

  .holder__name{position:absolute;left:27px;top:228px;font-size:38px;font-weight:500;letter-spacing:1px;color:var(--rust);line-height:1;white-space:nowrap}
  .holder__title{position:absolute;left:28px;top:278px;font-size:20px;color:var(--ink);line-height:1}

  .qr-space{position:absolute;left:28px;top:330px;width:86px;height:86px;border:2px dashed var(--qr-line);border-radius:6px}

  .contact{position:absolute;right:29px;color:var(--ink);font-size:21px;text-align:right;white-space:nowrap;line-height:1}
  .contact--addr1{top:246px}
  .contact--addr2{top:278px}
  .contact-row{position:absolute;right:29px;display:flex;align-items:center;gap:9px;font-size:21px;color:var(--ink);line-height:1;white-space:nowrap}
  .contact-row--phone{top:327px}
  .contact-row--mail{top:359px}
  .contact-row--web{top:391px}
  .contact-row svg{width:18px;height:18px;fill:var(--rust)}
</style>
</head>
<body>

<section class="card card--front">
  <div class="front-photo" role="img" aria-label="Warm orange-toned photo of a senior living art studio with easels, tables and chairs"></div>
  <div class="wordmark">
    <span class="wordmark__name">BRUVEL</span>
    <span class="wordmark__sub">LIVING</span>
  </div>
</section>

<section class="card card--back">
  <div class="wordmark">
    <span class="wordmark__name">BRUVEL</span>
    <span class="wordmark__sub">LIVING</span>
  </div>

  <div class="holder__name">Daniel Harlow</div>
  <div class="holder__title">General Manager</div>

  <div class="qr-space" role="img" aria-label="Optional space for a QR code"></div>

  <div class="contact contact--addr1">4810 Cedar Hollow Road, Suite 1204</div>
  <div class="contact contact--addr2">Oak Ridge, TX 77385</div>

  <div class="contact-row contact-row--phone">
    <span>(281) 555-0147</span>
    <svg viewBox="0 0 24 24" aria-hidden="true"><path d="M2 8c0-3 5-5 10-5s10 2 10 5v2h-5V8H7v2H2z"/><rect x="4" y="11" width="16" height="10" rx="2"/></svg>
  </div>
  <div class="contact-row contact-row--mail">
    <span>info@Bruvel-HQ.com</span>
    <svg viewBox="0 0 24 24" aria-hidden="true"><path d="M2 5h20v14H2z"/><path d="M2 5l10 8 10-8" fill="none" stroke="#fff" stroke-width="1.8"/></svg>
  </div>
  <div class="contact-row contact-row--web">
    <span>www.Bruvel-HQ.com</span>
    <svg viewBox="0 0 24 24" aria-hidden="true"><circle cx="12" cy="12" r="10"/><path d="M2 12h20M12 2c4 4 4 16 0 20M12 2c-4 4-4 16 0 20" fill="none" stroke="#fff" stroke-width="1.4"/></svg>
  </div>
</section>

</body>
</html>
```